Let's help people Kestrel with better hearing!

I need a business card for my private practice. I am a Dr. of Audiology and focus on hearing and tinnitus (ringing in the ears) treatment. My practice is named "Kestrel Hearing and Tinnitus Solutions". I want to communicate the idea of improved quality of life utilizing a natural color pallet Love the color turquoise as an accent. Want a professional look, while eye catching. I'm open to nontraditional design aesthetic. Something to get excited about and motivate people to improve their lives!

```html
<!DOCTYPE html>
<html lang="en">
<head>
<meta charset="utf-8">
<title>Kestrel Hearing &amp; Tinnitus Solutions – Business Card</title>
<link rel="stylesheet" href="https://fonts.googleapis.com/css2?family=Questrial&display=swap">
<style>
  :root {
    --page-bg: #eceeee;
    --card-bg: #ffffff;
    --teal: #5cc6cb;
    --teal-soft: #9fdcdf;
    --teal-pale: #d2eff0;
    --band: rgba(255, 255, 255, 0.78);
    --ink: #2aa0a8;
  }
  html, body {
    margin: 0;
    width: 1200px;
    height: 1000px;
    overflow: hidden;
    background: var(--page-bg);
    font-family: "Questrial", "Helvetica Neue", Arial, sans-serif;
  }
  .sheet {
    position: relative;
    width: 1200px;
    height: 1000px;
  }
  .card {
    position: absolute;
    left: 280px;
    width: 640px;
    height: 390px;
    background: var(--card-bg);
    overflow: hidden;
    box-shadow: 0 2px 10px rgba(0, 0, 0, 0.12);
  }
  .card--front { top: 70px; }
  .card--back { top: 540px; }
  .card__pattern {
    position: absolute;
    inset: 0;
  }
  .card--front .card__pattern {
    background: linear-gradient(125deg, var(--teal-soft) 0%, var(--teal-pale) 45%, var(--card-bg) 70%, var(--teal-pale) 100%);
  }
  .card--back .card__pattern {
    background: linear-gradient(110deg, var(--teal-pale) 0%, var(--teal-soft) 40%, var(--teal-pale) 70%, var(--teal-soft) 100%);
  }
  .card__band {
    position: absolute;
    left: 0;
    right: 0;
    background: var(--band);
  }
  .card--front .card__band { top: 120px; height: 160px; }
  .card--back .card__band { top: 110px; height: 170px; }

  .brand {
    position: absolute;
    right: 60px;
    top: 150px;
    text-align: center;
    color: var(--ink);
  }
  .brand__name {
    display: block;
    font-size: 52px;
    letter-spacing: 1px;
    line-height: 1;
  }
  .brand__rule {
    height: 1px;
    background: var(--ink);
    margin: 10px 0 6px;
  }
  .brand__tagline {
    display: block;
    font-size: 19px;
    letter-spacing: 0.5px;
    line-height: 1.25;
    text-transform: uppercase;
  }

  .contact {
    position: absolute;
    left: 50px;
    right: 40px;
    top: 132px;
    color: var(--ink);
  }
  .contact__name {
    font-size: 26px;
    letter-spacing: 2px;
    margin: 0 0 28px;
    font-weight: 400;
  }
  .contact__grid {
    display: grid;
    grid-template-columns: 1fr 1fr;
    gap: 12px 30px;
    font-size: 15px;
    letter-spacing: 0.5px;
  }
  .contact__item {
    display: flex;
    align-items: center;
    gap: 10px;
    white-space: nowrap;
  }
  .contact__icon {
    width: 16px;
    height: 16px;
    flex: none;
  }
</style>
</head>
<body>
<main class="sheet">

  <section class="card card--front" aria-label="Business card front">
    <div class="card__pattern" role="img" aria-label="Decorative pattern of overlapping turquoise arcs"></div>
    <div class="card__band"></div>
    <div class="brand">
      <span class="brand__name">Kestrel</span>
      <div class="brand__rule"></div>
      <span class="brand__tagline">Hearing &amp; Tinnitus<br>Solutions</span>
    </div>
  </section>

  <section class="card card--back" aria-label="Business card back">
    <div class="card__pattern" role="img" aria-label="Decorative pattern of overlapping turquoise arcs"></div>
    <div class="card__band"></div>
    <div class="contact">
      <h1 class="contact__name">Dr. Elena Marsh&nbsp;&nbsp;|&nbsp;&nbsp;Audiologist</h1>
      <div class="contact__grid">
        <span class="contact__item">
          <svg class="contact__icon" viewBox="0 0 16 16" aria-hidden="true"><path d="M4 1.5 L6 5 L4.6 6.4 A8 8 0 0 0 9.6 11.4 L11 10 L14.5 12 L13 14.5 A12 12 0 0 1 1.5 3 Z" fill="var(--ink)"/></svg>
          04 5521 0390
        </span>
        <span class="contact__item">
          <svg class="contact__icon" viewBox="0 0 16 16" aria-hidden="true"><rect x="1.5" y="3.5" width="13" height="9" fill="none" stroke="var(--ink)"/><path d="M1.5 3.5 L8 9 L14.5 3.5" fill="none" stroke="var(--ink)"/></svg>
          info@kestrelhearing.com.au
        </span>
        <span class="contact__item">
          <svg class="contact__icon" viewBox="0 0 16 16" aria-hidden="true"><circle cx="8" cy="8" r="6.5" fill="none" stroke="var(--ink)"/></svg>
          www.social.example/kestrelhearing
        </span>
        <span class="contact__item">
          <svg class="contact__icon" viewBox="0 0 16 16" aria-hidden="true"><rect x="1.5" y="2.5" width="13" height="9" fill="none" stroke="var(--ink)"/><path d="M5 14 H11" stroke="var(--ink)"/></svg>
          www.kestrelhearing.com.au
        </span>
      </div>
    </div>
  </section>

</main>
</body>
</html>
```